Lowen Academy

I need different posters for a high school that displays positive messaging and the school's core values.
Want the design to look sleek for high school aged children

1. Poster #1
CORE VALUES:
• RESPECT
• RESPONSIBILITY
• LEADERSHIP
• PRIDE
• COMMUNITY

2. Acronym posters for the school
Empathy
Zeal
Respect
Aspire

3. additional acronym poster
Encourage
Zenith
Relationships
Accountability

```html
<!DOCTYPE html>
<html lang="en">
<head>
<meta charset="utf-8">
<title>Lowen Academy – Core Values Poster</title>
<link href="https://fonts.googleapis.com/css2?family=Josefin+Sans:wght@700&family=Oswald:wght@700&display=swap" rel="stylesheet">
<style>
  :root {
    --backdrop: #d9d9db;
    --green-light: #8dc63f;
    --green-dark: #17773a;
    --magenta-light: #e91f7b;
    --magenta-dark: #96195c;
    --orange-light: #f7941d;
    --orange-dark: #ee3d36;
    --brown-light: #c69c6d;
    --brown-dark: #633a15;
    --blue-light: #00aeef;
    --blue-dark: #0c3a77;
    --badge-red: #c1202e;
    --label-white: #ffffff;
  }
  html, body {
    margin: 0;
    padding: 0;
    width: 1200px;
    height: 1200px;
    overflow: hidden;
    background: var(--backdrop);
  }
  .canvas {
    position: relative;
    width: 1200px;
    height: 1200px;
  }
  .poster {
    position: absolute;
    left: 234px;
    top: 81px;
    width: 732px;
    height: 1038px;
    box-shadow: 0 4px 14px rgba(0,0,0,0.25);
  }
  .value-label {
    font-family: "Josefin Sans", "Century Gothic", sans-serif;
    font-weight: 700;
    font-size: 26px;
    fill: var(--label-white);
    text-anchor: middle;
  }
  .badge-title {
    font-family: "Oswald", "Arial Narrow", sans-serif;
    font-weight: 700;
    font-size: 46px;
    fill: var(--label-white);
    text-anchor: middle;
  }
  .icon-slot {
    fill: var(--label-white);
    opacity: 0.22;
  }
</style>
</head>
<body>
<main class="canvas">
  <svg class="poster" viewBox="0 0 586 830" xmlns="http://www.w3.org/2000/svg" aria-label="Lowen Academy core values poster">
    <defs>
      <linearGradient id="grad-respect" x1="0" x2="1" y1="0" y2="0">
        <stop offset="0" stop-color="var(--green-light)"/>
        <stop offset="1" stop-color="var(--green-dark)"/>
      </linearGradient>
      <linearGradient id="grad-responsibility" x1="0" x2="1" y1="0" y2="0">
        <stop offset="0" stop-color="var(--magenta-light)"/>
        <stop offset="1" stop-color="var(--magenta-dark)"/>
      </linearGradient>
      <linearGradient id="grad-leadership" x1="0" x2="1" y1="0" y2="0">
        <stop offset="0" stop-color="var(--orange-light)"/>
        <stop offset="1" stop-color="var(--orange-dark)"/>
      </linearGradient>
      <linearGradient id="grad-pride" x1="0" x2="1" y1="0" y2="0">
        <stop offset="0" stop-color="var(--brown-light)"/>
        <stop offset="1" stop-color="var(--brown-dark)"/>
      </linearGradient>
      <linearGradient id="grad-community" x1="0" x2="1" y1="0" y2="0">
        <stop offset="0" stop-color="var(--blue-light)"/>
        <stop offset="1" stop-color="var(--blue-dark)"/>
      </linearGradient>
      <filter id="panel-shadow" x="-20%" y="-20%" width="140%" height="140%">
        <feDropShadow dx="0" dy="0" stdDeviation="6" flood-color="#000" flood-opacity="0.35"/>
      </filter>
    </defs>

    <g class="panels">
      <polygon class="panel panel-community" points="0,255 283,412 201,830 0,830" fill="url(#grad-community)"/>
      <polygon class="panel panel-pride" points="283,412 586,710 586,830 201,830" fill="url(#grad-pride)" filter="url(#panel-shadow)"/>
      <polygon class="panel panel-leadership" points="283,412 586,325 586,710" fill="url(#grad-leadership)" filter="url(#panel-shadow)"/>
      <polygon class="panel panel-responsibility" points="248,0 586,0 586,325 283,412" fill="url(#grad-responsibility)" filter="url(#panel-shadow)"/>
      <polygon class="panel panel-respect" points="0,0 248,0 283,412 0,255" fill="url(#grad-respect)" filter="url(#panel-shadow)"/>
    </g>

    <g class="value value-respect">
      <rect class="icon-slot" x="83" y="98" width="74" height="74" rx="14" role="img" aria-label="Icon: handshake inside a heart"/>
      <text class="value-label" x="120" y="220">RESPECT</text>
    </g>
    <g class="value value-responsibility">
      <rect class="icon-slot" x="393" y="108" width="74" height="74" rx="14" role="img" aria-label="Icon: open hand holding a group of people"/>
      <text class="value-label" x="430" y="237">RESPONSIBILITY</text>
    </g>
    <g class="value value-leadership">
      <rect class="icon-slot" x="450" y="400" width="60" height="60" rx="12" role="img" aria-label="Icon: person helping another up steps toward a flag"/>
      <text class="value-label" x="480" y="501">LEADERSHIP</text>
    </g>
    <g class="value value-community">
      <rect class="icon-slot" x="93" y="503" width="76" height="72" rx="14" role="img" aria-label="Icon: group of three people"/>
      <text class="value-label" x="131" y="622">COMMUNITY</text>
    </g>
    <g class="value value-pride">
      <rect class="icon-slot" x="355" y="605" width="72" height="80" rx="14" role="img" aria-label="Icon: raised fist"/>
      <text class="value-label" x="391" y="765">PRIDE</text>
    </g>

    <g class="core-badge" filter="url(#panel-shadow)">
      <circle cx="283" cy="412" r="97" fill="var(--badge-red)"/>
      <circle cx="283" cy="412" r="84" fill="none" stroke="var(--label-white)" stroke-width="4"/>
      <text class="badge-title" x="283" y="405">CORE</text>
      <text class="badge-title" x="283" y="451">VALUES</text>
    </g>
  </svg>
</main>
</body>
</html>
```